Website Required for Small Cyber Security Company

Require a website for Cyber Security company. I have logo which i will attach. Please use logo blue and white as a guide
Would ultimately like the site to have a technology theme with the following pages Landing page
Services
Contact
Careers

I can provide content for each of those pages in due course, until then happy for you to use dummy data to display purposes

Target Market(s)

Government

Industry/Entity Type

Cyber Security

Coding

Coded - Design and coding required

Number of Pages Required

4 page

Colors
0054AA
0677BA
7BADD7
CADEEF
E8F1F8

Requirements
Must have
• High quality finish and UX
Nice to have
• look and feel professional and not cheap

```html
<!DOCTYPE html>
<html lang="en">
<head>
<meta charset="utf-8">
<title>Harlow Reach – Next-Gen Endpoint Protection</title>
<link href="https://fonts.googleapis.com/css2?family=Inter:wght@300;400;500;600;700;800&display=swap" rel="stylesheet">
<style>
:root{
  --blue:#0a72d6;
  --blue-deep:#0054AA;
  --blue-head:#0a6fcf;
  --blue-soft:#7BADD7;
  --blue-pale:#CADEEF;
  --blue-wash:#E8F1F8;
  --dark:#2a2a2a;
  --dark-2:#3c3c3c;
  --grey-text:#8a8a8a;
  --body-text:#555;
  --white:#fff;
}
*{box-sizing:border-box;margin:0;padding:0}
html,body{width:1200px;height:4536px;overflow:hidden}
body{font-family:"Inter",Arial,sans-serif;color:var(--body-text);background:var(--white);position:relative}
section,header,footer{position:absolute;left:0;width:1200px}
a{color:inherit;text-decoration:none}

/* Hero */
.hero{top:0;height:576px;background:var(--blue);color:var(--white)}
.brand{position:absolute;left:56px;top:26px;width:140px;display:flex;flex-direction:column;align-items:center;gap:10px}
.brand-dot{width:44px;height:44px;border-radius:50%;background:var(--white)}
.brand-name{font-size:15px;font-weight:600;letter-spacing:.3px;text-transform:uppercase;white-space:nowrap}
.main-nav{position:absolute;left:229px;top:30px;display:flex}
.main-nav a{font-size:13px;font-weight:600;margin-right:52px}
.contact-bar{position:absolute;left:782px;top:30px;display:flex;align-items:center;font-size:13px;font-weight:600}
.contact-bar .sep{margin:0 26px;opacity:.8}
.contact-bar .mail{border-bottom:2px solid var(--white);padding-bottom:4px}
.hero h1{position:absolute;left:56px;top:196px;font-size:44px;font-weight:500;line-height:58px;letter-spacing:-.3px}
.hero .lede{position:absolute;left:56px;top:334px;font-size:27px;font-weight:300;line-height:37px}
.btn{position:absolute;display:flex;align-items:center;justify-content:center;font-size:17px}
.btn-view{left:56px;top:445px;width:196px;height:57px;background:var(--white);color:var(--blue)}
.btn-about{left:292px;top:445px;width:166px;height:57px;background:#2f8ae6;color:var(--white)}
.dashboard-shot{position:absolute;left:586px;top:174px;width:577px;height:370px;border-radius:4px;background:linear-gradient(90deg,#1e2a38 0 28px,#f7f8fa 28px,#ffffff 60%,#f1f3f6)}

/* Capabilities band */
.capabilities{top:576px;height:274px;display:flex}
.cap{width:300px;height:274px;text-align:center;color:#d8d8d8;padding-top:20px}
.cap:nth-child(odd){background:var(--dark-2)}
.cap:nth-child(even){background:var(--dark)}
.cap svg{display:block;margin:0 auto}
.cap h3{color:var(--white);font-size:18px;font-weight:700;margin-top:30px}
.cap p{font-size:13px;line-height:22px;letter-spacing:-.4px;margin:18px auto 0;width:200px}

/* Plans */
.plans{top:850px;height:637px}
.section-title{text-align:center;font-weight:700;color:var(--blue-head);letter-spacing:-.3px}
.plans .section-title{margin-top:55px;font-size:46px}
.plan{position:absolute;top:202px;width:347px;height:340px;border:1.5px solid var(--blue-soft);text-align:center}
.plan h4{font-size:21px;font-weight:400;color:#222;margin-top:26px}
.plan .platforms{font-size:13px;color:var(--grey-text);margin-top:18px;font-weight:300}
.plan svg{display:block;margin:28px auto 0}
.plan .terms{font-size:12px;color:#9a9a9a;font-weight:300;line-height:24px;margin-top:28px}
.plan .cta{display:inline-block;margin-top:12px;width:136px;height:38px;line-height:38px;border-radius:19px;background:#1b1b1b;color:var(--white);font-size:13px;font-weight:700}
.plan-left{left:51px}
.plan-right{left:801px}
.plan-featured{left:426px;top:167px;height:393px;background:var(--blue-wash);border:none}
.plan-featured .badge{height:36px;line-height:36px;background:var(--blue);color:var(--white);font-size:13px;font-weight:300}
.plan-featured h4{margin-top:24px}
.plan-featured .cta{background:var(--blue)}
.plan-featured .trial{display:block;margin-top:18px;font-size:13px;color:var(--blue);font-weight:600}

/* About band */
.business{top:1487px;height:426px;display:flex}
.business-copy{width:600px;background:var(--blue);color:var(--white);padding:58px 40px 0 49px}
.business-copy h2{font-size:40px;font-weight:700;letter-spacing:-.6px;white-space:nowrap}
.business-copy p{font-size:14px;line-height:22px;font-weight:500;margin-top:20px;letter-spacing:-.2px}
.business-copy p+p{margin-top:12px}
.learn{display:inline-block;margin-top:28px;border:2px solid var(--white);border-radius:18px;padding:7px 16px;font-size:13px;font-weight:700}
.business-photo{width:600px;background:linear-gradient(135deg,#c9d2dc 0%,#8d9aa8 45%,#5f6b78 70%,#b8c2cc 100%)}

/* Services */
.services{top:1913px;height:829px}
.services .section-title{margin-top:60px;font-size:46px}
.services .intro{text-align:center;font-size:22px;font-weight:300;line-height:42px;color:#777;margin-top:14px}
.service-grid{position:absolute;left:52px;top:255px;width:1096px;display:grid;grid-template-columns:repeat(4,1fr);grid-template-rows:256px 256px}
.service{text-align:center;padding-top:42px;border-right:2px dotted #9cc4e8}
.service:nth-child(4n){border-right:none}
.service:nth-child(-n+4){border-bottom:2px dotted #9cc4e8}
.service svg{display:block;margin:0 auto}
.service h5{font-size:17px;font-weight:700;color:#222;margin-top:18px}
.service p{font-size:12px;line-height:19px;color:#888;margin:20px auto 0;width:250px;letter-spacing:-.2px}

/* Testimonials */
.trusted{top:2742px;height:454px;background:var(--dark);color:var(--white)}
.trusted h2{text-align:center;font-size:44px;font-weight:700;margin-top:38px;letter-spacing:-.3px}
.quote{position:absolute;left:224px;top:153px;width:752px;font-size:12px;font-style:italic;font-weight:500;line-height:20px;text-indent:46px}
.quote-mark{position:absolute;left:224px;top:146px;font-size:60px;font-weight:800;line-height:40px;font-style:italic}
.endorse{position:absolute;top:248px;width:347px;height:159px;border:1.5px solid #555;display:flex;align-items:center;justify-content:center;gap:14px}
.endorse-1{left:51px}.endorse-2{left:426px}.endorse-3{left:801px}
.endorse .mark{width:26px;height:26px;background:var(--white)}
.endorse .mark.round{border-radius:50%}
.endorse .name{font-size:24px;font-weight:500}
.avatar{width:74px;height:74px;border-radius:50%;background:linear-gradient(160deg,#b79c88,#6d5a4e)}
.person b{display:block;font-size:18px;font-weight:700}
.person span{display:block;font-size:12px;margin-top:6px}

/* News */
.news{top:3196px;height:551px;background:var(--blue);color:var(--white)}
.news h2{text-align:center;font-size:44px;font-weight:700;margin-top:42px;letter-spacing:-.3px}
.article{position:absolute;top:148px;width:254px}
.article .thumb{height:188px}
.article h6{font-size:17px;font-weight:700;margin-top:18px}
.article time{display:block;font-size:11px;margin-top:20px}
.article p{font-size:11px;line-height:19px;margin-top:16px;letter-spacing:-.2px}
.article .more{display:block;font-size:11px;font-weight:700;margin-top:16px}
.a1{left:51px}.a2{left:333px}.a3{left:614px}.a4{left:894px}
.t1{background:linear-gradient(150deg,#8a5a36,#d9d2c6 55%,#3a3e4a)}
.t2{background:linear-gradient(170deg,#e6e6e4,#bdbab2 60%,#4a3a2c)}
.t3{background:linear-gradient(160deg,#7a4a36,#a66c52 50%,#3a3532)}
.t4{background:linear-gradient(150deg,#c6b6a2,#8a6a4e 55%,#d9cfc2)}

/* Customers */
.customers{top:3747px;height:387px}
.customers .section-title{margin-top:46px;font-size:44px}
.customers .intro{text-align:center;font-size:22px;font-weight:300;line-height:43px;color:#8a8a8a;margin-top:12px}
.client-row{position:absolute;left:152px;top:263px;display:flex}
.client{width:135px;text-align:center}
.client .chip{width:20px;height:20px;margin:0 auto;background:#b9cbe0;border-radius:50%}
.client span{display:block;margin-top:18px;font-size:13px;letter-spacing:1.2px;color:#777}

/* Footer */
.site-footer{top:4134px;height:402px;background:var(--dark);color:#bdbdbd}
.site-footer h6{font-size:17px;font-weight:700;color:var(--white)}
.f-contact{position:absolute;left:51px;top:57px;width:350px}
.f-about{position:absolute;left:426px;top:57px;width:350px}
.site-footer p{font-size:11px;line-height:19px;margin-top:20px}
.f-contact .line{font-size:11px;margin-top:18px}
.f-contact .line b{color:var(--white)}
.social{display:flex;gap:14px;margin-top:18px}
.social i{width:11px;height:11px;border-radius:50%;border:1.5px solid #bdbdbd}
.f-brand{position:absolute;left:860px;top:92px;width:220px;text-align:center;color:var(--white)}
.f-brand .ring{width:80px;height:80px;margin:0 auto;border-radius:50%;border:5px solid #2a86d6}
.f-brand .name{font-size:26px;font-weight:600;margin-top:16px;text-transform:uppercase;letter-spacing:.5px}
.f-rule{position:absolute;left:51px;top:330px;width:1097px;border-top:1px solid #444}
.copyright{position:absolute;top:360px;width:100%;text-align:center;font-size:11px}
</style>
</head>
<body>

<header class="hero">
  <a class="brand" href="#"><span class="brand-dot"></span><span class="brand-name">Harlow Reach</span></a>
  <nav class="main-nav">
    <a href="#">Service</a><a href="#">Careers</a><a href="#">Solutions</a><a href="#">Contact Us</a>
  </nav>
  <div class="contact-bar">
    <svg width="12" height="12" viewBox="0 0 24 24" style="margin-right:8px"><path fill="#fff" d="M6.6 10.8a15 15 0 0 0 6.6 6.6l2.2-2.2c.3-.3.7-.4 1-.2 1.1.4 2.3.6 3.6.6.6 0 1 .4 1 1V20c0 .6-.4 1-1 1A17 17 0 0 1 3 4c0-.6.4-1 1-1h3.5c.6 0 1 .4 1 1 0 1.3.2 2.5.6 3.6.1.3 0 .7-.2 1z"/></svg>
    <span>+1 (800) 555 01 20</span><span class="sep">|</span><a class="mail" href="#">info@harlowreach.example</a>
  </div>
  <h1>Next-Gen Endpoint<br>Protection Solution</h1>
  <p class="lede">Safeguard your enterprise from<br>advanced cyber threats</p>
  <a class="btn btn-view" href="#">View Serivce</a>
  <a class="btn btn-about" href="#">About us</a>
  <div class="dashboard-shot" role="img" aria-label="Screenshot of the threat dashboard showing incident details and a network graph of affected endpoints"></div>
</header>

<section class="capabilities">
  <div class="cap">
    <svg width="68" height="68" viewBox="0 0 68 68" fill="none" stroke="#fff" stroke-width="2"><circle cx="34" cy="34" r="30"/><circle cx="34" cy="34" r="21"/><circle cx="34" cy="34" r="12"/><line x1="34" y1="34" x2="56" y2="12"/><circle cx="34" cy="34" r="3" fill="#fff"/></svg>
    <h3>Detect</h3><p>Threats accurately prior to, during, and after execution whilst remaining resistant to false positives</p>
  </div>
  <div class="cap">
    <svg width="68" height="68" viewBox="0 0 68 68" fill="none" stroke="#fff" stroke-width="2"><path d="M34 4 8 14v18c0 16 11 27 26 32 15-5 26-16 26-32V14z"/><path d="M34 4v60"/></svg>
    <h3>Prevent</h3><p>Malware, exploits, unknown and blended cyberthreats, targeting enterprise network</p>
  </div>
  <div class="cap">
    <svg width="68" height="68" viewBox="0 0 68 68" fill="none" stroke="#fff" stroke-width="2"><circle cx="34" cy="34" r="30"/><path d="M14 34s8-11 20-11 20 11 20 11-8 11-20 11-20-11-20-11z"/><circle cx="34" cy="34" r="5" fill="#fff"/></svg>
    <h3>Monitor</h3><p>Suspicious activity on endpoints and cloud workloads, classify and alert on threats in a timely manner</p>
  </div>
  <div class="cap">
    <svg width="68" height="68" viewBox="0 0 68 68" fill="none" stroke="#fff" stroke-width="2"><circle cx="27" cy="26" r="19"/><path d="M40 40l22 22"/><path d="M17 24a10 10 0 0 1 10-9"/></svg>
    <h3>Investigate</h3><p>Threat's life cycle, form the moment of targeting to the post-infectionstage late detection</p>
  </div>
</section>

<section class="plans">
  <h2 class="section-title">Protect Your Assets with Harlow Reach</h2>
  <div class="plan plan-left">
    <h4>Embedded Systems</h4><div class="platforms">POS, ATM, SCADA</div>
    <svg width="86" height="72" viewBox="0 0 86 72" fill="none" stroke="#0a72d6" stroke-width="2"><rect x="22" y="4" width="60" height="46" rx="4"/><rect x="4" y="20" width="60" height="48" rx="4" fill="#fff"/><rect x="10" y="26" width="48" height="36"/></svg>
    <div class="terms">Requires annual commitment<br>Team Licenses available</div>
    <a class="cta" href="#">CHOOSE PLAN</a>
  </div>
  <div class="plan plan-featured">
    <div class="badge">Best Value</div>
    <h4>Enterprise Network</h4><div class="platforms">Desktop, Server, Laptop</div>
    <svg width="110" height="74" viewBox="0 0 110 74" fill="none" stroke="#0a72d6" stroke-width="2"><rect x="18" y="4" width="70" height="46" rx="3"/><path d="M44 50v10h18V50M36 62h34"/><rect x="4" y="30" width="22" height="40" rx="3" fill="#e8f1f8"/><rect x="78" y="26" width="28" height="44" rx="3" fill="#e8f1f8"/></svg>
    <div class="terms">Requires annual commitment<br>Team Licenses available</div>
    <a class="cta" href="#">BUY NOW</a>
    <a class="trial" href="#">Free Trial &gt;</a>
  </div>
  <div class="plan plan-right">
    <h4>Cloud Platforms</h4><div class="platforms">Nimbus Cloud, Stratus Grid</div>
    <svg width="80" height="74" viewBox="0 0 80 74" fill="none" stroke="#0a72d6" stroke-width="2"><path d="M18 50a14 14 0 0 1 2-28A20 20 0 0 1 58 18a14 14 0 0 1 4 32z"/><path d="M26 34v36M36 28v42M46 28v42M56 34v36"/></svg>
    <div class="terms">Requires annual commitment<br>Team Licenses available</div>
    <a class="cta" href="#">CHOOSE PLAN</a>
  </div>
</section>

<section class="business">
  <div class="business-copy">
    <h2>Protecting your Business</h2>
    <p>Sed ut perspiciatis unde omnis iste natus error sit voluptatem accusantium doloremque laudantium, totam rem aperiam, eaque ipsa quae ab illo inventore veritatis et quasi architecto beatae vitae dicta sunt explicabo. Nemo enim ipsam voluptatem quia voluptas.</p>
    <p>Sed ut perspiciatis unde omnis iste natus error sit voluptatem accusantium doloremque laudantium, totam rem aperiam, eaque ipsa quae ab illo inventore veritatis et quasi architecto beatae vitae dicta sunt explicabo</p>
    <a class="learn" href="#">LEARN MORE</a>
  </div>
  <div class="business-photo" role="img" aria-label="Photo of a team meeting in a bright glass-walled office"></div>
</section>

<section class="services">
  <h2 class="section-title">Our Services</h2>
  <p class="intro">The modern IT eosystem requires comprehensive and reliable protection against<br>advanced persistent threats (APTs) and proper mechanisms to mitigate the risk of data breach</p>
  <div class="service-grid">
    <div class="service">
      <svg width="70" height="50" viewBox="0 0 70 50" fill="none" stroke="#0a72d6" stroke-width="2"><path d="M16 46a12 12 0 0 1 0-24 18 18 0 0 1 34-6 14 14 0 0 1 4 30z"/></svg>
      <h5>Cloud Platforms</h5><p>Sed ut perspiciatis unde omnis iste natus error sit voluptate accusantium doloremqu.</p>
    </div>
    <div class="service">
      <svg width="56" height="56" viewBox="0 0 56 56" fill="none" stroke="#0a72d6" stroke-width="2"><circle cx="28" cy="28" r="6"/><circle cx="8" cy="8" r="5"/><circle cx="48" cy="8" r="5"/><circle cx="8" cy="48" r="5"/><circle cx="48" cy="48" r="5"/><circle cx="28" cy="6" r="3"/><path d="M12 12l12 12M44 12 32 24M12 44l12-12M44 44 32 32M28 9v13"/></svg>
      <h5>Networks</h5><p>Nemo qui enim ipsam voluptatem quia voluptas sit aspernatur aut odit aut fugit.</p>
    </div>
    <div class="service">
      <svg width="58" height="58" viewBox="0 0 58 58" fill="none" stroke="#0a72d6" stroke-width="2"><rect x="3" y="3" width="22" height="22" rx="2"/><rect x="33" y="3" width="22" height="22" rx="2"/><rect x="3" y="33" width="22" height="22" rx="2"/><path d="M44 34v20M34 44h20"/></svg>
      <h5>Applications</h5><p>Sed ut perspiciatis unde omnis iste natus error sit voluptatem accusantium quido et.</p>
    </div>
    <div class="service">
      <svg width="58" height="58" viewBox="0 0 58 58" fill="none" stroke="#0a72d6" stroke-width="2"><circle cx="9" cy="9" r="6"/><circle cx="29" cy="9" r="6"/><circle cx="49" cy="9" r="6"/><circle cx="9" cy="29" r="6"/><circle cx="29" cy="29" r="6"/><circle cx="49" cy="29" r="6"/><circle cx="9" cy="49" r="6"/><circle cx="29" cy="49" r="6"/><circle cx="49" cy="49" r="6"/></svg>
      <h5>Endpoints</h5><p>Ut enim ad minim veniam, quis nostrud etor exercitation ullamco laboris nisi ut aliquipe.</p>
    </div>
    <div class="service">
      <svg width="58" height="58" viewBox="0 0 58 58" fill="none" stroke="#0a72d6" stroke-width="2"><path d="M24 34 12 46a7 7 0 0 1-10-10l12-12a7 7 0 0 1 10 0"/><path d="M34 24 46 12a7 7 0 0 1 10 10L44 34a7 7 0 0 1-10 0"/><path d="M20 38l18-18"/></svg>
      <h5>Supply Chains</h5><p>Sed ut perspiciatis unde omnis iste natus error sit voluptate accusantium doloremqu.</p>
    </div>
    <div class="service">
      <svg width="52" height="58" viewBox="0 0 52 58" fill="none" stroke="#0a72d6" stroke-width="2"><ellipse cx="26" cy="9" rx="23" ry="7"/><path d="M3 9v40c0 4 10 7 23 7s23-3 23-7V9M3 22c0 4 10 7 23 7s23-3 23-7M3 35c0 4 10 7 23 7s23-3 23-7"/></svg>
      <h5>Systems</h5><p>Nemo qui enim ipsam voluptatem quia voluptas sit aspernatur aut odit aut fugit.</p>
    </div>
    <div class="service">
      <svg width="58" height="58" viewBox="0 0 58 58" fill="none" stroke="#0a72d6" stroke-width="2"><circle cx="29" cy="29" r="26"/><circle cx="29" cy="29" r="18"/><circle cx="29" cy="29" r="10"/><path d="M29 29 48 10"/></svg>
      <h5>Insider Threats</h5><p>Sed ut perspiciatis unde omnis iste natus error sit voluptatem accusantium quido et.</p>
    </div>
    <div class="service">
      <svg width="58" height="58" viewBox="0 0 58 58" fill="none" stroke="#0a72d6" stroke-width="2"><circle cx="29" cy="29" r="26"/><circle cx="29" cy="22" r="9"/><path d="M13 48c2-10 8-14 16-14s14 4 16 14"/></svg>
      <h5>Users</h5><p>Duis aute irure dolor in reprehenderit in ter voluptate velit esse cillum dolore eu fugiat.</p>
    </div>
  </div>
</section>

<section class="trusted">
  <h2>Trusted By Security Professionals</h2>
  <span class="quote-mark">“</span>
  <p class="quote">Provident, similique sunt in culpa qui officia deserunt mollitia animi, id est laborum et dolorum fuga eineem like temporalls. Et harum quidem rerum facilis est et expedita distinctio. Nam libero tempore, cum soluta nobis. At vero eos et samus et iusto odio qui blanditiis praesentium voluptatum deleniti atque corrupti quos jfont dolores et autem quibusdam et aut officis perferendis doloribus.</p>
  <div class="endorse endorse-1"><span class="mark"></span><span class="name">Brightova</span></div>
  <div class="endorse endorse-2"><div class="avatar" role="img" aria-label="Portrait photo of the reviewer"></div><div class="person"><b>Nora Feld</b><span>Creative Designer</span></div></div>
  <div class="endorse endorse-3"><span class="mark round"></span><span class="name">Meridian Works</span></div>
</section>

<section class="news">
  <h2>News &amp; Resources</h2>
  <article class="article a1"><div class="thumb t1" role="img" aria-label="Photo of a person carrying a leather bag up wooden stairs"></div><h6>Ullamcorper Parturien</h6><time>20 May, 2018</time><p>Morbi leo risus, porta ac consectur at eros. Maecenas sed diam eget risus varius blandit sit amet non.</p><a class="more" href="#">Read More &gt;</a></article>
  <article class="article a2"><div class="thumb t2" role="img" aria-label="Photo of a glass coffee carafe on a table"></div><h6>Excepteur Sint Occaecat</h6><time>20 May, 2018</time><p>Lorem ipsum dolor sit amet, consectetur adipiscing elit, sed do eiusmod tempor incididunt ut lab.</p><a class="more" href="#">Read More &gt;</a></article>
  <article class="article a3"><div class="thumb t3" role="img" aria-label="Photo of a cafe table against a brick wall"></div><h6>Neque Porro Quisquam</h6><time>20 May, 2018</time><p>Sed ut perspiciatis unde omnis iste natus error sit voluptatem accusantium doloremque laudanti.</p><a class="more" href="#">Read More &gt;</a></article>
  <article class="article a4"><div class="thumb t4" role="img" aria-label="Photo of a wallet on a table"></div><h6>Quis Autem Vel Eum</h6><time>20 May, 2018</time><p>Nemo enim ipsam voluptatem quia voluptas sit aspernatur aut odit aut fugit, sed quia conseuir.</p><a class="more" href="#">Read More &gt;</a></article>
</section>

<section class="customers">
  <h2 class="section-title">Our Customers</h2>
  <p class="intro">Recognized by Top 100 Index, Global 500<br>government and LEA agencies worldwide</p>
  <div class="client-row">
    <div class="client"><div class="chip"></div><span>KESTREL</span></div>
    <div class="client"><div class="chip"></div><span>ORVANE</span></div>
    <div class="client"><div class="chip"></div><span>PAYLO</span></div>
    <div class="client"><div class="chip"></div><span>LOREM</span></div>
    <div class="client"><div class="chip"></div><span>BRIGHTGRID</span></div>
    <div class="client"><div class="chip"></div><span>WAVECORE</span></div>
    <div class="client"><div class="chip"></div><span>MARKETA</span></div>
  </div>
</section>

<footer class="site-footer">
  <div class="f-contact">
    <h6>Contact Us</h6>
    <p>Maecenas etos sit amet, consectetur adipiscing elit. Terminal volutpat rutrum metro amet sollicitudin interdum.</p>
    <div class="line"><b>Phone:</b> +1 (800) 555 01 47</div>
    <div class="line"><b>Office:</b> Harbor Point Plaza</div>
    <div class="line"><b>Email:</b> info@harlowreach.example</div>
    <div class="social"><i></i><i></i><i></i><i></i><i></i></div>
  </div>
  <div class="f-about">
    <h6>About Company</h6>
    <p>Enim congue blandit. Lorem ipsum dolor sit amet, consectetur adipiscing elit. Quisque consectetur interdum finibus. Vestibulumante ipsum primis in faucibus orci. luctus et ultrices posuere.</p>
    <p>Cubilia cras blandit finibus ipsum, id porttitor arcu volutpat a. Integer iaculis erat nec justo malesuada faucibus vel tempus sapien. Vivamus aliquam euismod tristique.</p>
  </div>
  <div class="f-brand"><div class="ring"></div><div class="name">Harlow Reach</div></div>
  <div class="f-rule"></div>
  <div class="copyright">Copyright 2023. All Rights Reserved by Harlow Reach</div>
</footer>

</body>
</html>
```